High end boutique food product label

We are looking for a label design to be used on our range of high end food products. We don't have a design or colour scheme in mind and are interested to see what ideas are submitted.
We would like it to feel sophisticated, chic, and eye-catching.
All of our products are handmade in Australia using Australian ingredients.
The graphics for the label will need to be scaleable to be fit a variety of labels from small squat jars with labels sized 3.5cm high and 7cm wide, to tall thin bottles with labels that are 14cm high and 4.5cm wide.
We would be interested in working with the winning designer to create these different sized labels.
The label submitted for this project should be 14cm high and 4.5cm wide, it should include our logo (file supplied in .jpeg and .ai), the product name 'Extra Virgin Olive Oil' and the size '250ml'.
This is just the front label on a bottle, we are not expecting a rear label to be created currently.
You are welcome to use any fonts you think will look good but the fonts used in our logo are Allaina Medium and Bebas Kai Regular.

```html
<!DOCTYPE html>
<html lang="en">
<head>
<meta charset="UTF-8">
<title>Larkfield Pantry – Extra Virgin Olive Oil Label</title>
<link rel="stylesheet" href="https://fonts.googleapis.com/css2?family=Bebas+Neue&family=Playfair+Display:wght@700&display=swap">
<style>
  :root {
    --backdrop: #efefef;
    --label-white: #ffffff;
    --cocoa: #432818;
    --ink: #3a2216;
    --gold-light: #f3d77a;
    --gold-deep: #c89a2e;
    --sand: #b59f7c;
    --leaf-light: #dfe9cf;
    --leaf-mid: #a9c38e;
    --olive: #6f8f45;
  }
  * { margin: 0; padding: 0; box-sizing: border-box; }
  html, body {
    width: 1200px;
    height: 1000px;
    overflow: hidden;
    background: var(--backdrop);
  }
  .canvas {
    position: relative;
    width: 1200px;
    height: 1000px;
    display: flex;
    align-items: center;
    justify-content: center;
  }
  .label {
    position: relative;
    width: 284px;
    height: 885px;
    background: var(--label-white);
    overflow: hidden;
  }
  .label__header {
    position: absolute;
    top: 0; left: 0;
    width: 100%;
    height: 300px;
    background: var(--cocoa);
    display: flex;
    align-items: center;
    justify-content: center;
    padding-bottom: 40px;
  }
  .brand-name {
    font-family: "Playfair Display", serif;
    font-weight: 700;
    font-size: 34px;
    line-height: 1.05;
    color: var(--label-white);
    text-align: center;
    letter-spacing: 0.5px;
  }
  .label__wave {
    position: absolute;
    top: 255px; left: 0;
    width: 284px;
    height: 50px;
  }
  .product-title {
    position: absolute;
    top: 350px; left: 0;
    width: 100%;
    text-align: center;
  }
  .product-title__grade {
    font-family: "Bebas Neue", sans-serif;
    font-size: 25px;
    letter-spacing: 1.5px;
    color: var(--sand);
    line-height: 1;
  }
  .product-title__name {
    margin-top: 8px;
    font-family: "Playfair Display", serif;
    font-weight: 700;
    font-size: 46px;
    line-height: 1.05;
    color: var(--ink);
    letter-spacing: 1px;
  }
  .olive-branch {
    position: absolute;
    top: 515px; left: 0;
    width: 284px;
    height: 290px;
    background:
      radial-gradient(ellipse 30% 18% at 60% 55%, rgba(111,143,69,0.55), transparent 70%),
      radial-gradient(ellipse 60% 40% at 50% 50%, var(--leaf-mid), transparent 75%),
      radial-gradient(ellipse 75% 55% at 55% 50%, var(--leaf-light), transparent 80%);
  }
  .net-volume {
    position: absolute;
    bottom: 16px; left: 0;
    width: 100%;
    text-align: center;
    font-family: "Bebas Neue", sans-serif;
    font-size: 12px;
    letter-spacing: 0.8px;
    color: var(--ink);
  }
</style>
</head>
<body>
<main class="canvas">
  <article class="label">
    <header class="label__header">
      <h1 class="brand-name">Larkfield<br>Pantry</h1>
    </header>
    <svg class="label__wave" viewBox="0 0 284 50" preserveAspectRatio="none" aria-hidden="true">
      <defs>
        <linearGradient id="goldSweep" x1="0" y1="0" x2="1" y2="0">
          <stop offset="0" stop-color="var(--gold-deep)"/>
          <stop offset="0.45" stop-color="var(--gold-light)"/>
          <stop offset="1" stop-color="var(--gold-deep)"/>
        </linearGradient>
      </defs>
      <path d="M0 0 H284 V20 C230 14 190 22 150 30 C100 40 40 40 0 26 Z" fill="var(--cocoa)"/>
      <path d="M0 26 C40 40 100 40 150 30 C190 22 230 14 284 20 V30 C230 24 190 32 150 40 C100 50 40 48 0 40 Z" fill="url(#goldSweep)"/>
    </svg>
    <div class="product-title">
      <p class="product-title__grade">Extra Virgin</p>
      <h2 class="product-title__name">OLIVE<br>OIL</h2>
    </div>
    <div class="olive-branch" role="img" aria-label="Watercolour olive branch with green leaves and olives"></div>
    <p class="net-volume">Net Wet. 250ML</p>
  </article>
</main>
</body>
</html>
```